Ferncrest Dental, LLC business card project

Business card to be designed with current logo.
Dental office- please keep design of card that looks clean and professional.
Please include the following info:
Ferncrest Dental, LLC
Dr. Lorna Pettigrew
2871 Marlowe Street
Cedar Hollow, OR 97093
610-555-0193
ferncrestdental.office@examplemail.test
Hello everyone-
Reason: Just got back from overseas- will look at all designs and provide feedback. Thank you!
Reason: Polling my friends for the final selection-
thank you to all those that participated- so many talented designers!

```html
<!DOCTYPE html>
<html lang="en">
<head>
<meta charset="utf-8">
<title>Ferncrest Dental, LLC – Business Card</title>
<link href="https://fonts.googleapis.com/css2?family=Josefin+Sans:wght@300;400&family=Reenie+Beanie&display=swap" rel="stylesheet">
<style>
  :root {
    --page: #ffffff;
    --panel: #f2f2f2;
    --charcoal: #4d4e50;
    --card-edge: #9a9a9a;
    --paper: #ffffff;
    --ink: #3f3f41;
    --body-ink: #222222;
    --leaf: #72aa45;
    --white: #ffffff;
  }
  * { box-sizing: border-box; margin: 0; padding: 0; }
  html, body {
    width: 1200px;
    height: 348px;
    overflow: hidden;
    background: var(--page);
  }
  .sheet {
    position: relative;
    width: 1200px;
    height: 348px;
  }
  .panel {
    position: absolute;
    top: 0;
    width: 579px;
    height: 348px;
    background: var(--panel);
  }
  .panel--front { left: 0; }
  .panel--back { left: 621px; }

  .card {
    position: absolute;
    top: 18px;
    left: 18px;
    width: 543px;
    height: 311px;
  }

  /* Front */
  .card--front {
    background: var(--charcoal);
    border: 1px solid var(--card-edge);
    display: flex;
    align-items: center;
    justify-content: center;
  }
  .brand {
    display: flex;
    align-items: center;
    gap: 14px;
    margin-top: 12px;
  }
  .brand__dot {
    width: 24px;
    height: 24px;
    border-radius: 50%;
    background: var(--leaf);
    flex: none;
  }
  .brand__name {
    font-family: "Josefin Sans", "Century Gothic", sans-serif;
    font-weight: 300;
    font-size: 47px;
    color: var(--leaf);
    white-space: nowrap;
    padding-top: 7px;
  }

  /* Back */
  .card--back {
    left: 18px;
    width: 547px;
    background: var(--paper);
    border: 1px solid #111;
  }
  .doctor {
    position: absolute;
    top: 32px;
    left: 0;
    width: 100%;
    text-align: center;
    font-family: "Josefin Sans", "Century Gothic", sans-serif;
    font-weight: 400;
    font-size: 44px;
    letter-spacing: 4px;
    color: var(--ink);
    white-space: nowrap;
  }
  .phone-band {
    position: absolute;
    top: 113px;
    left: 0;
    width: 100%;
    height: 95px;
    background: var(--charcoal);
    display: flex;
    align-items: center;
    justify-content: center;
  }
  .phone {
    font-family: "Reenie Beanie", cursive;
    font-size: 64px;
    letter-spacing: 17px;
    margin-right: -17px;
    color: var(--white);
    line-height: 1;
    white-space: nowrap;
  }
  .address {
    position: absolute;
    top: 231px;
    left: 0;
    width: 100%;
    text-align: center;
    font-family: "Josefin Sans", "Century Gothic", sans-serif;
    font-weight: 300;
    font-size: 14px;
    line-height: 20.5px;
    letter-spacing: 1.5px;
    color: var(--body-ink);
    font-style: normal;
  }
</style>
</head>
<body>
  <main class="sheet">
    <section class="panel panel--front">
      <div class="card card--front">
        <div class="brand">
          <span class="brand__dot"></span>
          <span class="brand__name">Ferncrest Dental, LLC</span>
        </div>
      </div>
    </section>

    <section class="panel panel--back">
      <div class="card card--back">
        <h1 class="doctor">Dr. Lorna Pettigrew</h1>
        <div class="phone-band">
          <p class="phone">610-555-0193</p>
        </div>
        <address class="address">
          2871 marlowe street<br>
          cedar hollow, OR 97093<br>
          ferncrestdental.office@examplemail.test
        </address>
      </div>
    </section>
  </main>
</body>
</html>
```